Web Design Project

Looking to create a skin (just need PSD files) for our very simple publishing retail website (it only comprises of 2-3 pages but it has to be beautiful).

Also looking to create a logo in the style of the Quindle.com logo but slightly differant (ie has to be clear that they are related but not the same) The basic website has been built : http://narvetrix.com/inprogress/mm/WebDev/

The general look and feel which we are after is: the new tallyhive, the new yourcorner page, drift.fm (basically very web 2.0)

Full Brief Below:

The basic point of it is that as a student you can tell us which university you are at and then which course/degree you are studying and then up pops a list of all of the recommended text books which you can buy from bazaro.

A very similar site is but we are much simpler than them: www.coursetomeshelf.com We want it to be very minimalist and clean, like drift.fm

The colour scheme (though not the design) should also match the following website www.quindle.com You can ignore the input boxes on the bottom right and top right of the web page as they are not meant to be there.

The entire website only has three pages,: 1. Home Page, 2. Results page with Modules.3. Results Page with Books (when clicked on it should take you to Bazaro).

Target Market(s)

University Students

Industry/Entity Type

University

Requirements
Must have
• Specific Requirements:

1. Top of the page should be the new logo (similar to Quindle but differant, also needs a new name: e.g. Quindle Books or Quindle Reading, Quindle Physical, Quindle Old School, Quindle Books

2. Top of the page should be a paragraph of text and an image telling them what the website is.

3. Below that there should be two search boxes in a row, which list: University and Course. These should be auto fill (we have all the data, as per the attached spread sheet so they should only be able to select from these). When they select from these then they should be taken to another page listing all of the books, which pertain to this course & university (as per the website)

4. There should also be a general search bar in the top right hand corner this where they can just search normally for any book in our database. This will then produce a list of books wich you can then buy on bazaro

5. There should also be another area of text which relates to how we get the data and saying that we will give students free books if they email us their reading lists (if we don’t have them) and then they can email us to get a free book once we have checked that the data is correct. This should be an autofill box. Which they put their email into.

6. There should also be a box saying that students should sign up to Quindle.com (this should be on every page)

```html
<!DOCTYPE html>
<html lang="en">
<head>
<meta charset="utf-8">
<title>Quindle Books</title>
<link href="https://fonts.googleapis.com/css2?family=Hind:wght@300;400;600;700&family=Lora:ital@1&display=swap" rel="stylesheet">
<style>
  :root {
    --brand-blue: #41a6dc;
    --brand-blue-dark: #2f93cc;
    --button-blue: #3ea3dd;
    --panel-dark: #474d5a;
    --white: #ffffff;
    --field-text: #b4b7bd;
    --card-grey: #e6e6e6;
    --tweet-text: #8c8c8c;
    --link-orange: #e8603c;
    --book-label: #f2922c;
  }
  * { box-sizing: border-box; margin: 0; padding: 0; }
  html, body { width: 1200px; height: 1054px; overflow: hidden; }
  body { position: relative; background: var(--white); font-family: "Hind", sans-serif; color: var(--white); }
  .abs { position: absolute; }

  .top-line { left: 0; top: 0; width: 1200px; height: 5px; background: var(--brand-blue); z-index: 3; }
  .hero-photo { left: 0; top: 0; width: 1200px; height: 588px;
    background: linear-gradient(100deg, #8c7f72 0%, #a9a39b 30%, #6f6a66 55%, #2f2e30 80%, #1e1e22 100%); }

  .brand { left: 47px; top: 6px; width: 259px; height: 65px; background: var(--brand-blue);
    display: flex; align-items: center; gap: 12px; padding-left: 14px; z-index: 2; }
  .brand-mark { width: 34px; height: 34px; background: var(--white); }
  .brand-name { font-size: 30px; font-weight: 600; color: var(--white); line-height: 1; padding-top: 4px; }

  .site-search { left: 894px; top: 6px; width: 165px; height: 32px; background: var(--brand-blue);
    display: flex; align-items: center; padding-left: 8px; gap: 8px; }
  .site-search-field { width: 126px; height: 16px; background: var(--white); border-radius: 8px; }
  .sign-up { left: 1062px; top: 6px; width: 91px; height: 32px; background: var(--white);
    color: var(--brand-blue); font-size: 16px; font-weight: 600; text-align: center; line-height: 36px; }

  .slide-arrows { left: 568px; top: 238px; }

  .hero-title { left: 706px; top: 148px; width: 460px; font-size: 33px; font-weight: 600; line-height: 41px; }
  .hero-text { left: 706px; top: 282px; width: 460px; font-size: 23px; font-weight: 300; line-height: 31px; }

  .finder-shadow { left: 250px; top: 620px; width: 700px; height: 60px; border-radius: 50%;
    background: radial-gradient(ellipse at center, rgba(0,0,0,0.18) 0%, rgba(0,0,0,0) 70%); }
  .finder { left: 235px; top: 435px; width: 730px; height: 210px; background: var(--white); padding: 8px; }
  .finder-inner { width: 100%; height: 100%; background: var(--panel-dark); position: relative; }
  .finder-field { top: 20px; width: 329px; height: 52px; background: var(--white); color: var(--field-text);
    font-size: 18px; line-height: 56px; padding-left: 15px; }
  .finder-field svg { position: absolute; right: 16px; top: 19px; }
  .field-university { left: 16px; }
  .field-faculty { left: 370px; }
  .finder-button { left: 190px; top: 100px; width: 335px; height: 75px; background: var(--button-blue);
    font-size: 23px; font-weight: 600; text-align: center; line-height: 80px; border-radius: 2px; }
  .slide-dots { left: 583px; top: 674px; }

  .footer-band { left: 0; top: 702px; width: 1200px; height: 352px; background: var(--brand-blue); }

  .tweet-tab-back { left: 94px; top: 759px; width: 318px; height: 18px; background: var(--card-grey); }
  .tweet-tab-mid { left: 71px; top: 774px; width: 370px; height: 19px; background: var(--card-grey); }
  .tweet-card { left: 48px; top: 792px; width: 427px; height: 161px; background: var(--white); }
  .tweet-pointer { left: 214px; top: 952px; }
  .tweet-shadow { left: 60px; top: 962px; width: 400px; height: 30px; border-radius: 50%;
    background: radial-gradient(ellipse at center, rgba(0,0,0,0.15) 0%, rgba(0,0,0,0) 70%); }
  .tweet-avatar { left: 44px; top: 67px; width: 36px; height: 38px; border: 1px solid #e2e2e2; border-radius: 4px;
    display: flex; align-items: center; justify-content: center; }
  .tweet-avatar span { width: 18px; height: 18px; background: #d9392b; }
  .tweet-text { left: 93px; top: 38px; width: 310px; font-family: "Lora", serif; font-style: italic;
    font-size: 16px; line-height: 20px; color: var(--tweet-text); }
  .tweet-text a { color: var(--link-orange); text-decoration: none; }
  .tweet-text .short-link { color: #c0392b; }
  .tweet-time { left: 0; top: 118px; width: 427px; text-align: center; font-family: "Lora", serif;
    font-style: italic; font-size: 14px; color: #b0b0b0; }
  .tweet-source { left: 375px; top: 122px; width: 20px; height: 20px; border-radius: 50%; background: #c4c4c4; }

  .books-heading { left: 551px; top: 734px; font-size: 24px; font-weight: 600; }
  .books-widget { left: 553px; top: 782px; width: 300px; height: 242px; }
  .shelf-label { font-size: 9px; font-weight: 700; color: var(--book-label); }
  .shelf-more { font-size: 8px; color: var(--book-label); }
  .shelf-arrow { width: 11px; height: 22px; background: #e4e4e4; border-radius: 3px; }
  .book { width: 37px; height: 55px; }
  .book-caption { font-size: 7px; line-height: 8px; color: #dbeaf4; width: 50px; }

  .hashtag { left: 913px; top: 734px; font-size: 27px; font-weight: 700; letter-spacing: 0.5px; }
  .hashtag-note { left: 913px; top: 772px; width: 260px; font-size: 13px; font-weight: 600; line-height: 18px; }
  .news-heading { left: 953px; top: 830px; font-size: 24px; font-weight: 600; }
  .news-list { left: 943px; top: 873px; list-style: none; font-size: 23px; font-weight: 300; line-height: 30.6px; }
</style>
</head>
<body>
  <div class="abs hero-photo" role="img" aria-label="Photo of students studying together at laptops in a university library"></div>
  <div class="abs top-line"></div>

  <header>
    <div class="abs brand"><span class="brand-mark"></span><span class="brand-name">quindle books</span></div>
    <div class="abs site-search">
      <span class="site-search-field"></span>
      <svg width="14" height="14" viewBox="0 0 14 14"><circle cx="5.5" cy="5.5" r="4" fill="none" stroke="#fff" stroke-width="2"/><line x1="8.5" y1="8.5" x2="12.5" y2="12.5" stroke="#fff" stroke-width="2.4" stroke-linecap="round"/></svg>
    </div>
    <a class="abs sign-up">Sign Up</a>
  </header>

  <svg class="abs slide-arrows" width="64" height="30" viewBox="0 0 64 30">
    <polyline points="17,5 8,15 17,25" fill="none" stroke="#fff" stroke-width="4" stroke-linecap="round" stroke-linejoin="round"/>
    <polyline points="46,5 55,15 46,25" fill="none" stroke="#fff" stroke-width="4" stroke-linecap="round" stroke-linejoin="round"/>
  </svg>

  <h1 class="abs hero-title">Quindle books is a new way to access the resources you need for your course.</h1>
  <p class="abs hero-text">Just select your university and subject from the lists below to access your reading list.</p>

  <div class="abs finder-shadow"></div>
  <section class="abs finder">
    <div class="finder-inner">
      <div class="abs finder-field field-university">Select your university
        <svg width="15" height="15" viewBox="0 0 15 15"><circle cx="6" cy="6" r="4.5" fill="none" stroke="#cfd1d5" stroke-width="1.6"/><line x1="9.5" y1="9.5" x2="13.5" y2="13.5" stroke="#cfd1d5" stroke-width="2"/></svg>
      </div>
      <div class="abs finder-field field-faculty">Select your faculty
        <svg width="15" height="15" viewBox="0 0 15 15"><circle cx="6" cy="6" r="4.5" fill="none" stroke="#cfd1d5" stroke-width="1.6"/><line x1="9.5" y1="9.5" x2="13.5" y2="13.5" stroke="#cfd1d5" stroke-width="2"/></svg>
      </div>
      <div class="abs finder-button">Search for my books</div>
    </div>
  </section>
  <svg class="abs slide-dots" width="34" height="10" viewBox="0 0 34 10">
    <circle cx="5" cy="5" r="4" fill="#555"/><circle cx="17" cy="5" r="4" fill="#555"/><circle cx="29" cy="5" r="4" fill="#555"/>
  </svg>

  <footer class="abs footer-band"></footer>

  <div class="abs tweet-shadow"></div>
  <div class="abs tweet-tab-back"></div>
  <div class="abs tweet-tab-mid"></div>
  <article class="abs tweet-card">
    <div class="abs tweet-avatar"><span></span></div>
    <p class="abs tweet-text">We're giving away one ticket to <a>@brightconf</a> (<a class="short-link">lnk.to/qR7vKp</a>, Germany). To get a chance of winning it, just tweet us!</p>
    <div class="abs tweet-time">58 minutes ago</div>
    <span class="abs tweet-source"></span>
  </article>
  <svg class="abs tweet-pointer" width="22" height="14" viewBox="0 0 22 14"><polygon points="0,0 22,0 11,13" fill="#fff"/></svg>

  <h2 class="abs books-heading">Hottest Books on Bazaro</h2>
  <section class="abs books-widget">
    <div class="abs shelf-label" style="left:0;top:2px;">Course Essentials</div>
    <div class="abs shelf-more" style="left:270px;top:3px;">Shop more</div>
    <div class="abs shelf-arrow" style="left:0;top:24px;"></div>
    <div class="abs shelf-arrow" style="left:289px;top:24px;"></div>
    <div class="abs book" style="left:21px;top:13px;background:#6a5fb5;"></div>
    <div class="abs book" style="left:86px;top:13px;background:#6d62b8;"></div>
    <div class="abs book" style="left:153px;top:13px;background:#675cb2;"></div>
    <div class="abs book" style="left:220px;top:13px;background:#6b60b6;"></div>
    <div class="abs book-caption" style="left:16px;top:70px;">New Title</div>
    <div class="abs book-caption" style="left:81px;top:70px;">New Title</div>
    <div class="abs book-caption" style="left:148px;top:70px;">New Title</div>
    <div class="abs book-caption" style="left:215px;top:70px;">New Title</div>

    <div class="abs shelf-label" style="left:0;top:134px;">Study Skills</div>
    <div class="abs shelf-more" style="left:270px;top:135px;">Shop more</div>
    <div class="abs shelf-arrow" style="left:0;top:158px;"></div>
    <div class="abs shelf-arrow" style="left:289px;top:158px;"></div>
    <div class="abs book" style="left:21px;top:145px;background:#7b5aa8;"></div>
    <div class="abs book" style="left:86px;top:145px;background:#e0a22a;"></div>
    <div class="abs book" style="left:153px;top:145px;background:#4f9a54;"></div>
    <div class="abs book" style="left:220px;top:145px;background:#3e8fb0;"></div>
    <div class="abs book-caption" style="left:16px;top:204px;">New Title</div>
    <div class="abs book-caption" style="left:81px;top:204px;">New Title</div>
    <div class="abs book-caption" style="left:148px;top:204px;">New Title</div>
    <div class="abs book-caption" style="left:215px;top:204px;">New Title</div>
  </section>

  <h2 class="abs hashtag">#QUINDLEBOOKS</h2>
  <p class="abs hashtag-note">remember to follow us for freebook giveaways and other goodies</p>
  <h2 class="abs news-heading">News Feed</h2>
  <ul class="abs news-list">
    <li>- Article 1</li>
    <li>- Article 2</li>
    <li>- Article 3</li>
    <li>- Article 4</li>
    <li>- Article 6</li>
  </ul>
</body>
</html>
```